Improve our BRX Data Analysis website and create a landing page for it

We have a website that hosts a number of web applications which allow users to perform various online statistical analysis. Here is the link to the website:

The website is made by Wordpress using a free template. From the front page of the website, the users can select the type of analysis they would like to perform (which leads to an individual page of this particular analysis), then follow a link that connects to the web application itself.

The current front page shows only a few selections for the type of the analysis and they are arranged quite randomly.

Now the problem is - we actually have a large number of functionality that we want to show in the front page, so that the users can get a quick glance of what's possible and what can be done from our website. By functionality we grouped them in the following manner:

Data View
- Data Table
- Data Summary

Data Preparation
- Filter Column
- Arrange Column
- Create New Column

Pivot Table
- Table
- Table Barchart
- Heatmap
- Row Heatmap
- Column Heatmap
- Line Chart
- Bar Chart
- Stacked Barchart
- Area Chart

Graphic Tools
- Histogram
- Density Chart
- Line Chart
- Point Chart
- Boxplot
- Geomap
- Vortel Drift Chart

Hypothesis Testing
(p-value)
- t Test
- Exact Test
- Chi-square Test
- ANOVA

Statistical Modelling
- Simple Linear Regression
- Multiple Linear Regression
- Generalized Linear Model
- Logistic Regression
- Poisson Regression
- Survival Analysis
- Cox Proportional Hazards Model
- Longitudinal Analysis
- Time Series Analysis

Clustering
- K-means Clustering
- Principal Component Analysis
- Factor Analysis
- Heatmap
- Machine Learning

Sample Size Calculator
- Continuous Outcome
- Binary Outcome

Instructor's Teaching Toolkit
- tbd
- tbd

Equation Solver
- tbd
- tbd

Requirements:
1. We want a new landing page that systematically and responsively shows the above product lines in a neat and modern way, with graphic display and preferably some text explanation (something similar to our current front page. you can use placeholders for the graphics for now and we will replace them later). We have also attached a few screenshots of the web applications here so that you can get a feel of what it looks like and how it works.

2. Each type of analysis will have its own page as well (once the user clicks through it from the landing page). From this page the users can link to the relevant web application directly (currently we use the iframe for the link). In this page there should be places for video instruction and gif instructions of how to use the app (we will make the instructions later, so just a place holder). There should also be placeholder for help documents. In each of these pages, there should be places where users can cross link to other type of analysis.

3. You are free to use our current template, or use your own one. At the end of the project, you will need to teach us how to make further modifications on our own.

Look forward to your cool ideas!
BRX

```html
<!DOCTYPE html>
<html lang="en">
<head>
<meta charset="utf-8">
<title>BRX Data Analysis</title>
<link href="https://fonts.googleapis.com/css2?family=Open+Sans:wght@400;600;700&family=Oswald:wght@300&family=Pirata+One&display=swap" rel="stylesheet">
<style>
:root{
  --nav:#1c1c1c;
  --ink:#444;
  --blue:#1b9bd7;
  --brand:#1e7fd8;
  --green:#2fbd3a;
  --lime:#00ff22;
  --red:#ff2a1a;
  --chip:#1a1a1a;
  --rule:#cfcfcf;
  --footer:#262626;
}
*{box-sizing:border-box;margin:0;padding:0}
html,body{width:739px;height:1200px;overflow:hidden;background:#fff}
body{font-family:"Open Sans",Arial,sans-serif;color:var(--ink)}
.page{position:relative;width:739px;height:1200px;overflow:hidden}
.abs{position:absolute}

/* navbar */
.navbar{position:absolute;left:0;top:0;width:739px;height:35px;background:var(--nav)}
.navbar span{position:absolute;top:10px;font-size:7.2px;color:#bbb;white-space:nowrap}
.navbar .home{color:#fff;font-weight:700}
.navbar .active{background:#000;color:#fff;font-weight:600;top:0;height:35px;line-height:25px;padding:0 6px}
.navbar .more{color:#fff;font-weight:700}
.acct{color:#fff!important;font-weight:600}
.acct i{display:inline-block;width:14px;height:14px;background:#ddd;vertical-align:middle;margin-right:4px}
.dropdown{position:absolute;background:#fff;border:1px solid #ddd;box-shadow:0 2px 4px rgba(0,0,0,.2);z-index:5;padding:3px 0}
.dropdown li{list-style:none;font-size:6.6px;color:#333;padding:0 9px;height:12.7px;line-height:12.7px;white-space:nowrap}
.dropdown li.hl{background:#eee}
.dropdown hr{border:0;border-top:1px solid #ddd;margin:4px 0}

/* header */
.logo{left:8px;top:42px;display:flex;align-items:center;gap:6px}
.logo i{width:16px;height:16px;background:var(--brand)}
.logo b{font-size:26px;color:var(--brand);font-weight:700;letter-spacing:4px}
.site-title{left:255px;top:40px;font-size:17px;color:#222}
.order{left:424px;top:41px;width:67px;height:21px;border:1px solid #ccc;border-radius:3px;font-size:8px;line-height:19px;text-align:center;color:#333}

/* slider */
.slider{left:78px;top:76px;width:557px;height:179px;background:linear-gradient(160deg,#c9d8e0 0%,#5fd6e6 40%,#1fb8cf 65%,#bcd3dc 100%)}
.slider .caption{position:absolute;left:0;right:0;top:113px;text-align:center;color:#fff;font-size:16px;line-height:19px;text-shadow:0 1px 2px rgba(0,0,0,.4)}
.slider .dots{position:absolute;top:157px;left:257px;display:flex;gap:3px}
.slider .dots i{width:4px;height:4px;border:1px solid #fff;border-radius:50%}
.slider .dots i:first-child{background:#fff}
.arrow{position:absolute;top:84px;width:8px;height:8px;border-left:2px solid #fff;border-bottom:2px solid #fff}
.share{position:absolute;background:var(--green);border-radius:4px}
.intro{left:78px;top:265px;width:555px;font-size:6.6px;line-height:9.5px;color:#333}

/* search row */
.category{left:75px;top:288px;width:202px;height:27px;background:var(--brand);color:#fff;font-weight:700;font-size:10px;line-height:27px;padding-left:5px;border-radius:2px}
.go{left:282px;top:288px;width:41px;height:27px;background:#65bd3b;color:#e6e04a;font-weight:700;font-size:12px;line-height:27px;text-align:center}
.lens{left:423px;top:279px;width:93px;height:31px;background:linear-gradient(90deg,#e3ebf3,#7f8fa6 50%,#e0e7ef)}
.search{left:525px;top:281px;width:204px;height:27px;border:3px solid #2a2e36;background:#2a2e36}
.search .field{position:absolute;left:3px;top:3px;width:140px;height:15px;background:#fff}
.search .btn{position:absolute;right:3px;top:3px;width:50px;height:15px;background:#6ab52e;color:#fff;font-size:8px;font-weight:700;text-align:center;line-height:15px}

/* content */
.rule-top{left:5px;top:323px;width:592px;height:2px;background:var(--rule)}
.rule-side{left:596px;top:323px;width:2px;height:806px;background:var(--rule)}
.card{position:absolute;width:176px}
.thumb{height:108px;border:1px solid #ddd;box-shadow:0 1px 3px rgba(0,0,0,.25);background:#fff;overflow:hidden}
.thumb svg{display:block;width:100%;height:100%}
.card h3{font-size:8.4px;color:var(--blue);font-weight:600;margin-top:2px;line-height:10px}
.card p{font-size:7px;line-height:10.8px;color:#444}
.card p a{color:var(--blue)}

.badge{left:0;top:0}
.like-circle{position:absolute;left:5px;top:5px;width:37px;height:37px;border-radius:50%;background:var(--blue);color:#fff;text-align:center;font-size:7px;font-weight:700;line-height:9px;padding-top:10px}
.date{position:absolute;right:4px;top:6px;text-align:right;font-size:14px;color:#333;line-height:13px}
.date small{display:block;font-size:10px}
.badge-name{position:absolute;left:50px;top:55px;font-size:8px;color:#333}

/* side menu */
.side{left:607px;top:325px;width:125px}
.side li{list-style:none;height:20.5px;margin-bottom:1.8px;background:var(--lime);font-family:"Pirata One",serif;font-size:13px;color:#1a3bd8;line-height:20px;padding-left:3px;border:1px solid #ddd}
.side li.on{background:var(--red);color:#ffea00}

.social{position:absolute;left:612px;width:115px;background:#e6f1f8;box-shadow:0 1px 3px rgba(0,0,0,.3)}
.social h4{color:#fff;font-size:8px;text-align:center;height:20px;line-height:20px;letter-spacing:.5px}
.sbtn{display:inline-block;border:1px solid #bbb;background:#fff;font-size:8px;font-weight:700;color:#335;padding:1px 5px;border-radius:2px}
.count{display:inline-block;border:1px solid #bbb;background:#fff;font-size:7px;padding:1px 4px;margin-left:3px}

/* share + pager */
.shares{left:16px;top:1020px;display:flex;gap:5px}
.shares i{width:21px;height:24px}
.printpdf{left:176px;top:1025px;width:70px;height:14px;border:1px solid #9c6;border-radius:3px;background:#eef7e0;font-size:7px;color:#555;text-align:center;line-height:12px}
.pager{left:286px;top:1020px;display:flex;gap:5px}
.pager span{background:#111;color:#fff;font-size:7.4px;font-weight:600;height:17px;line-height:17px;padding:0 5px}
.pager .n{width:24px;text-align:center;padding:0}
.pager .cur{background:var(--blue)}

.cats-title{left:37px;top:1060px;font-size:8.4px;color:#222}
.cats-rule{left:37px;top:1077px;width:380px;height:1px;background:#333}
.chips{left:37px;display:flex;gap:3px}
.chips span{background:var(--chip);color:#fff;font-size:6.3px;padding:0 3px;height:12px;line-height:12px;border:1px solid #555}
.chips .cur{background:var(--blue)}

.rule-bottom{left:0;top:1127px;width:739px;height:1px;background:#aaa}
.footer{left:0;top:1130px;width:739px;height:50px;background:var(--footer)}
.footer span{position:absolute;left:512px;top:18px;font-family:"Oswald",sans-serif;font-weight:300;font-size:9px;color:#888}
</style>
</head>
<body>
<div class="page">

  <nav class="navbar">
    <span class="home" style="left:22px">Home</span>
    <span style="left:54px">Data View ▾</span>
    <span style="left:107px">Data Preparation ▾</span>
    <span class="active" style="left:171px">Pivot Table ▾</span>
    <span style="left:232px">Graphic Tools ▾</span>
    <span style="left:296px">Hypothesis Testing ▾</span>
    <span style="left:375px">Statistical Modelling ▾</span>
    <span style="left:455px">Clustering ▾</span>
    <span class="more" style="left:505px">More ▾</span>
    <span style="left:542px">Portfolio ▾</span>
    <span style="left:586px">About</span>
    <span style="left:619px">Contact</span>
    <span class="acct" style="left:667px;top:8px">▾ <i></i>Accounts</span>
  </nav>

  <ul class="dropdown" style="left:171px;top:27px;width:78px">
    <li>Table</li><li>Table Barchart</li><li>Heatmap</li><li>Row Heatmap</li><li>Column Heatmap</li><li>Line Chart</li><li>Bar Chart</li><li>Stacked Barchart</li><li>Area Chart</li>
  </ul>
  <ul class="dropdown" style="left:498px;top:27px;width:107px">
    <li>Sample Size Calculator</li><li>Instructor's Teaching Toolkit</li><li>Equation Solver</li><li>Others</li>
  </ul>
  <ul class="dropdown" style="left:655px;top:30px;width:78px">
    <li>Log In</li><li class="hl">Register here</li><hr><li>Users</li><hr><li>Partners login</li><hr><li>Admin</li>
  </ul>

  <div class="abs logo"><i></i><b>BRX</b></div>
  <div class="abs site-title">BRX Data Analysis</div>
  <div class="abs order">Order Now</div>

  <div class="abs slider" role="img" aria-label="3D surface plot of statistical data in teal and purple">
    <i class="arrow" style="left:40px;transform:rotate(45deg)"></i>
    <i class="arrow" style="right:40px;transform:rotate(-135deg)"></i>
    <div class="caption">First Image the description will be added<br>here.</div>
    <div class="dots"><i></i><i></i><i></i><i></i><i></i><i></i></div>
    <div class="share" style="left:510px;top:138px;width:42px;height:34px">
      <svg viewBox="0 0 42 34" width="42" height="34"><g fill="#fff" stroke="#fff" stroke-width="2.5"><line x1="14" y1="17" x2="27" y2="10"/><line x1="14" y1="17" x2="27" y2="24"/><circle cx="14" cy="17" r="4"/><circle cx="27" cy="10" r="4"/><circle cx="27" cy="24" r="4"/></g></svg>
    </div>
  </div>

  <p class="abs intro">We provide simple online user interface for complex data analysis and visualization. All you need to do is just to upload your data from your hard disk, then everything else is only a few mouse clicks.</p>

  <div class="abs category">Select a data Category &nbsp;▾</div>
  <div class="abs go">Go</div>
  <div class="abs lens" role="img" aria-label="Magnifying glass over data strip"></div>
  <div class="abs search"><div class="field"></div><div class="btn">Search</div></div>

  <div class="abs rule-top"></div>
  <div class="abs rule-side"></div>

  <!-- row 1 -->
  <div class="card" style="left:16px;top:328px">
    <div class="thumb" role="img" aria-label="Hazard ratio plots by age and sex" style="background:linear-gradient(90deg,#fff,#e8e8f8 30%,#fff 50%,#e8e8f8 80%,#fff)"></div>
    <h3>Cox Proportional Hazards Model</h3>
    <p>Proportional hazards models are a class of survival models in statistics. Survival models relate the time that passes before some event occurs ...( <a>learn more</a> )</p>
  </div>
  <div class="card" style="left:201px;top:328px">
    <div class="thumb" role="img" aria-label="Two scatter plots with fitted regression lines" style="background:linear-gradient(135deg,#fff 20%,#f3e9d9 50%,#fff 80%)"></div>
    <h3>Generalized Linear Models</h3>
    <p>The generalized linear model (GLM) is a flexible generalization of ordinary linear regression that allows for response variables that have ....( <a>learn more</a> )</p>
  </div>
  <div class="card" style="left:386px;top:328px">
    <div class="thumb" role="img" aria-label="Statistical data analysis 3D density peak" style="background:radial-gradient(circle at 62% 45%,#e64a2e 0,#f5c52e 12%,#2a73d6 30%,#061436 70%)"></div>
    <h3>Heatmap</h3>
    <p>A heat map is a graphical representation of data where the individual values contained in a matrix are represented as colors. Draw heatmap....( <a>learn more</a> )</p>
  </div>

  <!-- row 2 -->
  <div class="card" style="left:16px;top:501px">
    <div class="thumb" role="img" aria-label="Data table of diamond measurements" style="background:repeating-linear-gradient(180deg,#fff 0 5px,#eef0f4 5px 6px)"></div>
    <h3>Heatmap</h3>
    <p>A heat map is a graphical representation of data where the individual values contained in a matrix are represented as colors. Draw heatmap....( <a>learn more</a> )</p>
  </div>
  <div class="card" style="left:201px;top:501px">
    <div class="thumb" role="img" aria-label="Clustered heatmap in blue and red" style="background:linear-gradient(90deg,#9ec5e6 0%,#c7dcee 40%,#e9967a 60%,#c9413a 75%,#a9cbe8 100%)"></div>
    <h3>Heatmap</h3>
    <p>A heat map is a graphical representation of data where the individual values contained in a matrix are represented as colors. Draw heatmap....( <a>learn more</a> )</p>
  </div>
  <div class="card" style="left:386px;top:501px">
    <div class="thumb">
      <svg viewBox="0 0 176 108" preserveAspectRatio="none">
        <polyline fill="none" stroke="#e8743b" stroke-width="1" points="6,90 14,75 20,82 28,62 34,70 42,55 50,66 58,48 66,58 74,40 82,52 90,36 98,46 106,30 114,42 122,24 130,36 138,22 146,30 154,18 162,26 170,20"/>
        <polyline fill="none" stroke="#2aa39a" stroke-width="1" points="6,86 14,80 20,70 28,72 34,60 42,64 50,52 58,56 66,44 74,50 82,38 90,44 98,32 106,40 114,28 122,34 130,24 138,30 146,20 154,28 162,18 170,24"/>
        <line x1="6" y1="98" x2="172" y2="98" stroke="#999" stroke-width=".5"/>
      </svg>
    </div>
    <h3>Heatmap</h3>
    <p>A heat map is a graphical representation of data where the individual values contained in a matrix are represented as colors. Draw heatmap....( <a>learn more</a> )</p>
  </div>

  <!-- row 3 -->
  <div class="card" style="left:16px;top:677px">
    <div class="thumb badge" style="border:0;box-shadow:none;position:relative">
      <div class="like-circle">31<br>Like</div>
      <div class="date">26<small>Mar 2015</small></div>
      <div class="badge-name">BRX Data Analysis</div>
      <div class="share" style="left:127px;top:67px;width:42px;height:34px">
        <svg viewBox="0 0 42 34" width="42" height="34"><g fill="#fff" stroke="#fff" stroke-width="2.5"><line x1="14" y1="17" x2="27" y2="10"/><line x1="14" y1="17" x2="27" y2="24"/><circle cx="14" cy="17" r="4"/><circle cx="27" cy="10" r="4"/><circle cx="27" cy="24" r="4"/></g></svg>
      </div>
    </div>
    <h3>Heatmap</h3>
    <p>A heat map is a graphical representation of data where the individual values contained in a matrix are represented as colors. Draw heatmap....( <a>learn more</a> )</p>
  </div>
  <div class="card" style="left:204px;top:677px">
    <div class="thumb" role="img" aria-label="Vortel Drift Chart bubble plot of life expectancy" style="background:radial-gradient(circle at 25% 30%,#f2b66b 0,#7fb3e0 12%,#fff 28%),radial-gradient(circle at 30% 80%,#f08a9a 0,#fff 15%)"></div>
    <h3>Heatmap</h3>
    <p>A heat map is a graphical representation of data where the individual values contained in a matrix are represented as colors. Draw heatmap....( <a>learn more</a> )</p>
  </div>
  <div class="card" style="left:392px;top:677px">
    <div class="thumb">
      <svg viewBox="0 0 176 108">
        <line x1="49" y1="10" x2="49" y2="36" stroke="#333"/><line x1="49" y1="78" x2="49" y2="96" stroke="#333"/>
        <line x1="125" y1="28" x2="125" y2="40" stroke="#333"/><line x1="125" y1="70" x2="125" y2="84" stroke="#333"/>
        <rect x="10" y="36" width="80" height="42" fill="#f26c63" stroke="#333"/>
        <rect x="89" y="40" width="80" height="30" fill="#17c0c4" stroke="#333"/>
        <line x1="10" y1="53" x2="90" y2="53" stroke="#333"/><line x1="89" y1="56" x2="169" y2="56" stroke="#333"/>
      </svg>
    </div>
    <h3>Heatmap</h3>
    <p>A heat map is a graphical representation of data where the individual values contained in a matrix are represented as colors. Draw heatmap....( <a>learn more</a> )</p>
  </div>

  <!-- row 4 -->
  <div class="card" style="left:16px;top:850px">
    <div class="thumb">
      <svg viewBox="0 0 176 108" preserveAspectRatio="none">
        <path d="M0,100 C40,60 70,30 90,20 C110,30 130,50 176,80 L176,108 L0,108Z" fill="#a8dfe0" stroke="#555" stroke-width=".6"/>
        <path d="M0,60 C30,70 60,75 90,60 C120,50 150,80 176,90 L176,108 L0,108Z" fill="#f5b4b0" fill-opacity=".75" stroke="#555" stroke-width=".6"/>
      </svg>
    </div>
    <h3>Heatmap</h3>
    <p>A heat map is a graphical representation of data where the individual values contained in a matrix are represented as colors. Draw heatmap....( <a>learn more</a> )</p>
  </div>
  <div class="card" style="left:204px;top:850px">
    <div class="thumb">
      <svg viewBox="0 0 176 108" preserveAspectRatio="none">
        <g fill="#17b8c2"><rect x="8" y="82" width="14" height="26"/><rect x="22" y="70" width="14" height="38"/><rect x="36" y="76" width="14" height="32"/><rect x="50" y="50" width="14" height="58"/><rect x="64" y="34" width="14" height="74"/><rect x="78" y="46" width="14" height="62"/><rect x="92" y="20" width="14" height="88"/><rect x="106" y="6" width="14" height="102"/><rect x="120" y="40" width="14" height="68"/><rect x="134" y="60" width="14" height="48"/><rect x="148" y="80" width="14" height="28"/></g>
        <g fill="#f26c63"><rect x="8" y="96" width="14" height="12"/><rect x="22" y="92" width="14" height="16"/><rect x="36" y="94" width="14" height="14"/><rect x="50" y="86" width="14" height="22"/><rect x="64" y="80" width="14" height="28"/><rect x="78" y="84" width="14" height="24"/><rect x="92" y="76" width="14" height="32"/><rect x="106" y="72" width="14" height="36"/><rect x="120" y="82" width="14" height="26"/><rect x="134" y="88" width="14" height="20"/><rect x="148" y="96" width="14" height="12"/></g>
      </svg>
    </div>
    <h3>Heatmap</h3>
    <p>A heat map is a graphical representation of data where the individual values contained in a matrix are represented as colors. Draw heatmap....( <a>learn more</a> )</p>
  </div>
  <div class="card" style="left:392px;top:850px">
    <div class="thumb" role="img" aria-label="Scatter of sized dots in orange and green" style="background:radial-gradient(circle at 30% 40%,#f7c2a8 0,#fff 25%),radial-gradient(circle at 70% 60%,#b8e0c4 0,#fff 30%)"></div>
    <h3>Heatmap</h3>
    <p>A heat map is a graphical representation of data where the individual values contained in a matrix are represented as colors. Draw heatmap....( <a>learn more</a> )</p>
  </div>

  <!-- side -->
  <ul class="abs side">
    <li>Side Menu 1</li><li>Side Menu 2</li><li class="on">Side Menu 3</li><li>Side Menu 4</li><li>Side Menu 5</li><li>Side Menu 6</li><li>Side Menu 7</li><li>Side Menu 8</li><li>Side Menu 9</li><li>Side Menu 10</li>
  </ul>

  <div class="social" style="top:577px;height:52px">
    <h4 style="background:#3a67b0">LINKBOARD</h4>
    <div style="padding:5px 0 0 20px"><span class="sbtn" style="background:#3a67b0;color:#fff">Like</span><span class="count">1k</span></div>
  </div>
  <div class="social" style="top:636px;height:78px">
    <h4 style="background:#1b9bd7">CHIRPER</h4>
    <div style="padding:7px 0 0 6px"><span class="sbtn">Follow</span></div>
    <div style="padding:7px 0 0 6px"><span class="sbtn">Post</span><span class="count">0</span></div>
  </div>

  <!-- share + pager -->
  <div class="abs shares" aria-label="Share links">
    <i style="background:#3b5a9a"></i><i style="background:#28a8e0"></i><i style="background:#d8432e"></i><i style="background:#0e76a8"></i><i style="background:#ccc"></i><i style="background:var(--green)"></i>
  </div>
  <div class="abs printpdf">Print &nbsp;PDF</div>
  <div class="abs pager">
    <span>|&lt;&lt; start</span><span>&lt; previous</span><span class="n">1</span><span class="n">2</span><span class="n cur">3</span><span class="n">4</span><span class="n">5</span><span>Next &gt;</span><span>Last &gt;&gt;|</span>
  </div>

  <div class="abs cats-title">Search by Categories</div>
  <div class="abs cats-rule"></div>
  <div class="abs chips" style="top:1089px"><span>All Categories</span><span>Data View</span><span class="cur">Data Preparation</span><span>Pivot Table</span><span>Graphic Tools</span><span>Hypothesis Testing</span></div>
  <div class="abs chips" style="top:1108px"><span>Statistical Modelling</span><span>Clustering</span><span>Sample Size Calculator</span><span>Instructor's Teaching Toolkit</span><span>Equation Solver</span></div>

  <div class="abs rule-bottom"></div>
  <footer class="abs footer"><span>All rights reserved © 2015 - BRX Data Analysis</span></footer>
</div>
</body>
</html>
```